'Tarvel' a financial/crypto-currency exchange in the middle east

On the card we need 1) Name 2) title 3) email address 4) phone number using the same colors and theme as the logo. On one side we just want the logo and we want the whole card to be in blue (same blue as logo) with the logo in the back being white.
Industry/Entity Type
Financial

```html
<!DOCTYPE html>
<html lang="en">
<head>
<meta charset="utf-8">
<title>Tarvel – Business Card</title>
<link rel="stylesheet" href="https://fonts.googleapis.com/css2?family=Open+Sans:wght@400;600;700&display=swap">
<style>
  :root {
    --brand-blue: #0f67ae;
    --brand-blue-edge: #0b5894;
    --white: #ffffff;
    --soft-white: #e6f0f8;
    --backdrop: #e6e8eb;
  }
  * { box-sizing: border-box; margin: 0; padding: 0; }
  html, body {
    width: 1200px;
    height: 970px;
    overflow: hidden;
    background: var(--backdrop);
    font-family: "Open Sans", Arial, sans-serif;
  }
  .card {
    position: absolute;
    left: 173px;
    top: 270px;
    width: 855px;
    height: 476px;
    background: var(--brand-blue);
    border: 1.5px solid var(--brand-blue-edge);
    border-radius: 22px;
    color: var(--soft-white);
  }
  .brand {
    position: absolute;
    left: 42px;
    top: 50px;
    display: flex;
    align-items: center;
    gap: 20px;
  }
  .brand-dot {
    width: 94px;
    height: 94px;
    border-radius: 50%;
    border: 4px solid var(--white);
  }
  .brand-name {
    font-size: 44px;
    font-weight: 700;
    color: var(--white);
    letter-spacing: 0.5px;
  }
  .person-name {
    position: absolute;
    left: 42px;
    top: 180px;
    font-size: 23px;
    line-height: 30px;
    font-weight: 700;
    color: var(--white);
    letter-spacing: 0.5px;
  }
  .person-title {
    position: absolute;
    left: 42px;
    top: 208px;
    font-size: 19px;
    line-height: 28px;
  }
  .contact-list {
    position: absolute;
    left: 42px;
    top: 247px;
    list-style: none;
  }
  .contact-list li {
    display: flex;
    align-items: center;
    gap: 8px;
    height: 26.5px;
    font-size: 19px;
  }
  .contact-list svg { width: 18px; height: 18px; fill: var(--soft-white); }
  .address {
    position: absolute;
    left: 42px;
    top: 357px;
    font-size: 19px;
    line-height: 26px;
  }
  .social {
    position: absolute;
    left: 42px;
    top: 401px;
    display: flex;
    align-items: center;
    gap: 6px;
    font-size: 19px;
    line-height: 26px;
  }
  .social-dot {
    width: 23px;
    height: 23px;
    border-radius: 50%;
    background: var(--white);
  }
  .social-handle { margin-left: 6px; }
  .emblem {
    position: absolute;
    left: 402px;
    top: 30px;
    width: 415px;
    height: 415px;
    border-radius: 50%;
    border: 12px solid var(--white);
    display: flex;
    align-items: center;
    justify-content: center;
  }
  .emblem-name {
    font-size: 72px;
    font-weight: 700;
    color: var(--white);
    letter-spacing: 1px;
  }
</style>
</head>
<body>
  <div class="card">
    <div class="brand">
      <div class="brand-dot"></div>
      <div class="brand-name">Tarvel</div>
    </div>

    <div class="person-name">NORA HADDAD</div>
    <div class="person-title">Managing Director</div>

    <ul class="contact-list">
      <li>
        <svg viewBox="0 0 24 24" aria-hidden="true"><path d="M3 9c0-3 4-5 9-5s9 2 9 5v2h-5V9c-1-.6-2.4-1-4-1s-3 .4-4 1v2H3zM6 12h12l2 8H4z"/></svg>
        + 000 000 000
      </li>
      <li>
        <svg viewBox="0 0 24 24" aria-hidden="true"><path d="M7 2h10a1 1 0 0 1 1 1v18a1 1 0 0 1-1 1H7a1 1 0 0 1-1-1V3a1 1 0 0 1 1-1zm1 3v13h8V5zm4 14.2a1 1 0 1 0 0 2 1 1 0 0 0 0-2z"/></svg>
        + 000 000 000
      </li>
      <li>
        <svg viewBox="0 0 24 24" aria-hidden="true"><path d="M2 5h20v14H2zm2 2v.5l8 5.5 8-5.5V7zm0 2.9V17h16V9.9l-8 5.4z"/></svg>
        Nora@tarvel.com
      </li>
      <li>
        <svg viewBox="0 0 24 24" aria-hidden="true"><path d="M12 2a10 10 0 1 0 0 20 10 10 0 0 0 0-20zm-1 2.1V7H8.2A8 8 0 0 1 11 4.1zM6.8 9H11v2H4.1a8 8 0 0 1 2.7-2zM4.1 13H11v2H6.8a8 8 0 0 1-2.7-2zm4.1 4H11v2.9A8 8 0 0 1 8.2 17zM13 19.9V17h2.8a8 8 0 0 1-2.8 2.9zm0-4.9v-2h6.9a8 8 0 0 1-2.7 2zm0-4V9h4.2a8 8 0 0 1 2.7 2zm0-4V4.1A8 8 0 0 1 15.8 7z"/></svg>
        www.tarvel.com
      </li>
    </ul>

    <div class="address">215 Harbor Lane, FL 33019</div>

    <div class="social">
      <span class="social-dot"></span>
      <span class="social-dot"></span>
      <span class="social-dot"></span>
      <span class="social-handle">@Tarvel</span>
    </div>

    <div class="emblem">
      <span class="emblem-name">Tarvel</span>
    </div>
  </div>
</body>
</html>
```